Flyer To Solicit Donations for a Good Cause

Hi. I am running the distance of a marathon race to solicit donations for a charitable cause. I need a well designed flyer to help me solicit support from friends and others. The copy for the flyer is attached. There is a significant amount of written text so it will need to be laid out in a way that is easy to read but also mixes well with some good images and design appeal. I am open to creative ideas. I have also attached my photo and a photo of me shaking hands with Mayor Derlin of Delphi and president of the Brastow Harmonic Fellowship. Also there are some photos of the areas. These photos don't have to be used except for the one of me shaking hands with the Mayor and a caption underneath it. Otherwise, I am open to other stock photos or graphics. Feel free to contact me if you have questions. Thank you !

Update: ONE SIDED FLYER

• Photo of the Mayor and Toby with the caption identifying us; All of the copy/text.

```html
<!DOCTYPE html>
<html lang="en">
<head>
<meta charset="utf-8">
<title>A Special Journey</title>
<link rel="stylesheet" href="https://fonts.googleapis.com/css2?family=Marcellus&family=Cinzel:wght@400;500&family=Oswald:wght@300;400&family=Crimson+Text:ital,wght@0,400;1,400&family=Vollkorn:wght@800;900&display=swap">
<style>
  :root {
    --paper: #f1eedb;
    --card: #ffffff;
    --ink: #1a1a1a;
    --body: #2b2b2b;
    --muted: #6b6b6b;
    --link: #d98a3a;
    --band: rgba(45, 45, 45, 0.72);
    --band-text: #e9e9e9;
    --rule: #d9d9d9;
  }
  * { box-sizing: border-box; margin: 0; padding: 0; }
  html, body { width: 900px; height: 1200px; overflow: hidden; background: var(--paper); }
  .flyer {
    position: relative; width: 900px; height: 1200px; background: var(--paper);
    font-family: "Crimson Text", Georgia, serif; color: var(--body);
  }
  .card { position: absolute; left: 16px; top: 18px; width: 868px; height: 1124px; background: var(--card); overflow: hidden; }
  .title {
    position: absolute; left: 42px; top: 62px; z-index: 2; white-space: nowrap;
    font-family: "Marcellus", "Times New Roman", serif; font-weight: 400;
    font-size: 60px; letter-spacing: 0.5px; color: var(--ink); line-height: 1;
  }
  .subtitle {
    position: absolute; left: 44px; top: 126px; z-index: 2; white-space: nowrap;
    font-family: "Cinzel", Georgia, serif; font-size: 16.3px; letter-spacing: 0; color: var(--ink);
  }
  .landscape {
    position: absolute; left: 0; top: 157px; width: 868px; height: 342px;
    background: linear-gradient(180deg, #5e6469 0%, #8d9397 18%, #bfc4c6 26%, #4f5a52 36%, #55604f 60%, #6e6a4f 82%, #8a7e5e 100%);
  }
  .portrait {
    position: absolute; left: 652px; top: 38px; width: 196px; height: 222px; z-index: 1;
    background: linear-gradient(180deg, #cfc8c0 0%, #9b8d82 45%, #2f3237 75%, #23262b 100%);
    border-radius: 95px 95px 4px 4px;
  }
  .run-title {
    position: absolute; left: 0; width: 868px; top: 268px; text-align: center;
    font-family: "Oswald", "Arial Narrow", sans-serif; font-weight: 300; font-size: 19px;
    letter-spacing: 0.8px; color: #f4f4f4;
  }
  .run-byline {
    position: absolute; left: 0; width: 868px; top: 296px; text-align: center;
    font-family: "Cinzel", Georgia, serif; font-size: 12px; letter-spacing: 0.6px; color: #e6e6e6;
  }
  .intro-band {
    position: absolute; left: 0; top: 407px; width: 868px; height: 92px; background: var(--band);
    display: flex; align-items: center; justify-content: center; text-align: center;
    font-family: "Marcellus", Georgia, serif; font-size: 17.4px; line-height: 1.25;
    letter-spacing: 0.3px; color: var(--band-text); padding: 0 40px;
  }
  .column { position: absolute; top: 526px; }
  .column--left { left: 31px; width: 414px; }
  .column--right { left: 531px; width: 305px; }
  .divider {
    position: absolute; left: 478px; top: 516px; width: 6px; height: 500px;
    background: linear-gradient(90deg, rgba(0,0,0,0.10), rgba(0,0,0,0));
    border-left: 1px solid var(--rule);
  }
  h2 {
    font-family: "Vollkorn", Georgia, serif; font-weight: 900; font-size: 15.5px;
    color: var(--ink); letter-spacing: 0.2px; margin-bottom: 14px;
  }
  p, li { font-style: italic; font-size: 13.4px; line-height: 1.33; text-align: justify; }
  .link { font-style: italic; font-size: 13.4px; color: var(--link); text-decoration: none; }
  .handshake {
    display: block; margin-top: 20px; width: 414px; height: 130px;
    background: linear-gradient(90deg, #e7e3da 0%, #b9c6d3 35%, #8fa0b3 55%, #e3dfd6 100%);
  }
  .caption { font-style: italic; font-size: 7.5px; color: var(--muted); margin-top: 8px; text-align: left; }
  .concept { margin-top: 20px; }
  .steps { list-style: none; margin-top: 22px; }
  .steps li { position: relative; padding-left: 23px; margin-bottom: 17px; }
  .steps li::before {
    content: ""; position: absolute; left: 2px; top: 7px; width: 5px; height: 5px;
    border-radius: 50%; background: var(--ink);
  }
  .support { position: absolute; left: 0; width: 868px; top: 1022px; text-align: center; }
  .support h2 { margin-bottom: 2px; }
  .support p { text-align: center; }
</style>
</head>
<body>
<div class="flyer">
  <div class="card">
    <div class="landscape" role="img" aria-label="Panoramic photo of the mountains around Delphi under a cloudy sky"></div>
    <div class="portrait" role="img" aria-label="Portrait photo of Toby Hallam in a dark jacket"></div>
    <h1 class="title">A SPECIAL JOURNEY</h1>
    <div class="subtitle">FOR YOUR SPECIFIC PRAYERS &amp; FOR AN IMPORTANT ANCIENT CAUSE</div>
    <div class="run-title">26 MILES JOURNEY - APRIL 2016</div>
    <div class="run-byline">BY TOBY HALLAM</div>
    <div class="intro-band">This coming April 2016 Toby Hallam will make a special running journey of 26 miles through the ancient lands of Apollo and Athena at Delphi on Mt. Parnassus in Greece.</div>

    <section class="column column--left">
      <h2>Written Prayers &amp; Petitions</h2>
      <p>Toby will adorn his running outfit with special cloth strips that will contain written prayers and petitions of people who will sponsor his journey by making a charitable donation to the Brastow Harmonic Fellowship, an organization that preserves the land and the Delphic culture.</p>
      <a class="link" href="#">www.brastow-harmonic-fellowship.org</a>
      <div class="handshake" role="img" aria-label="Photo of Toby Hallam shaking hands with Mayor Derlin in an office"></div>
      <div class="caption">Toby Hallam with Mayor Derlin of Delphi and president of the Brastow Harmonic Fellowship</div>
      <div class="concept">
        <h2>The Concept</h2>
        <p>The concept is simple and very powerful: as Toby runs,your written prayer on a cloth strip will flow and emanate in the wind --- being blessed by the spirits of this ancient and magical land --- asking unto the wind that your prayer be answered. This type of prayer practice dates back to ancient times. The Tibetan culture commonly uses prayer flags with special mantras and symbols.</p>
      </div>
    </section>

    <div class="divider"></div>

    <section class="column column--right">
      <h2>Here is how to get your prayer started:</h2>
      <ul class="steps">
        <li>Decide what you want your prayer, petition or intention to be.</li>
        <li>Define your prayer, petition or intention by writing it down.</li>
        <li>Refine it is concise, clear&amp; specific. (18 words or less is ideal for each strip cloth).</li>
        <li>Contact Toby at thallam@hallamreeve.com and tell him how many prayer cloth strips you wish to obtain. Toby will then send you the cloth for you to write your prayer and send back to him or he will write out the prayer for you. Toby can also answer any questions you may have.</li>
        <li>A minimum donation of $50 for each prayer cloth is requested. Checks can be made to the “Hallam Reeve Trust Account/Brastow Harmonic Fellowship” and mail to Toby T. Hallam, Hallam Reeve PLC, 1480 Elm Crest Avenue, Ste. 212 Linden, Virginia 23299 or though PayNest instructions sent by email from Toby as requested.</li>
      </ul>
    </section>

    <section class="support">
      <h2>The Support</h2>
      <p>Will you make a prayer for yourself or a loved and support a good cause?</p>
    </section>
  </div>
</div>
</body>
</html>
```